IT Company that provides secure IT solutions and services to our customers

We need business cards and a logo for a new IT Solutions company just created based in Kuala Lumpur, Malaysia. But will also be serving other countries in the region. We provide secure data, voice solutions on mobile platforms. Our first offering is encrypted voice and data solutions for Orbis OS, Droidex, Panelix and Bramblex devices.

Target Market(s)

large organizations Govt, Police, Defence, Anti-corruption, Legal, highly regulated industries such as Health-care, Financial, Banking, Insurance,

Industry/Entity Type

Information Technology

Contact Information for Business Card

VornaxIT (Logo - colour is ORBEL blue)Dariush Pelo Managing Director Vornax IT Sdn. Bhd.5th Floor, Block F, Wisma LBD,No.14 Jalan Seri Mewah,50470, Kuala LumpurMalaysia

Font styles to use
Sans Serif

Colors
3176b5
ec1f27
fbed22

Requirements
Must have
• VornaxIT all in Blue like ORBEL blue. A logo design perhaps a play of VI, K with a dangling T (colour can be any)
Nice to have
• I want a clean crisp card, not too busy, easy to read.

```html
<!DOCTYPE html>
<html lang="en">
<head>
<meta charset="utf-8">
<title>VornaxIT Business Card</title>
<link rel="stylesheet" href="https://fonts.googleapis.com/css2?family=Saira+Semi+Condensed:wght@400;700&display=swap">
<style>
  :root {
    --brand-blue: #3176b5;
    --brand-red: #ec1f27;
    --paper: #ffffff;
    --backdrop: #e9e6e1;
    --text-light: #ffffff;
    --font-main: "Saira Semi Condensed", "Arial Narrow", sans-serif;
  }
  * { box-sizing: border-box; margin: 0; padding: 0; }
  html, body { width: 939px; height: 1200px; overflow: hidden; }
  body { background: var(--backdrop); font-family: var(--font-main); position: relative; }

  .card {
    position: absolute;
    left: 103px;
    width: 745px;
    height: 448px;
    background: var(--paper);
    overflow: hidden;
    box-shadow: 0 2px 6px rgba(0,0,0,0.18);
  }
  .card--front { top: 111px; }
  .card--back { top: 653px; }
  .card__shapes { position: absolute; inset: 0; width: 100%; height: 100%; }

  .brand { position: absolute; display: flex; align-items: center; gap: 10px; }
  .brand__dot { width: 22px; height: 22px; border-radius: 50%; }
  .brand__name { font-weight: 700; font-size: 46px; line-height: 1; color: var(--brand-blue); letter-spacing: -0.5px; }
  .card--front .brand { left: 92px; top: 48px; }
  .card--front .brand__dot { background: var(--brand-red); }
  .card--back .brand { left: 132px; top: 300px; }
  .card--back .brand__dot { background: var(--brand-blue); }

  .person { position: absolute; right: 122px; top: 104px; text-align: right; color: var(--brand-blue); }
  .person__name { font-weight: 700; font-size: 25px; line-height: 1.3; }
  .person__title { font-weight: 400; font-size: 25px; line-height: 1.3; }

  .contact { position: absolute; right: 118px; top: 212px; list-style: none; color: var(--text-light); font-size: 22px; }
  .contact__item { display: flex; justify-content: flex-end; align-items: center; height: 31px; gap: 8px; }
  .contact__icon { width: 20px; height: 20px; flex: none; }
  .contact__item--address { height: auto; margin-top: 12px; align-items: flex-start; line-height: 31px; text-align: right; }
  .contact__item--address .contact__icon { margin-top: 6px; height: 32px; }

  .tagline {
    position: absolute; left: 0; right: 0; top: 100px;
    text-align: center; color: var(--text-light);
    font-size: 28px; line-height: 38px; font-weight: 400;
  }
</style>
</head>
<body>

<section class="card card--front" aria-label="Business card front">
  <svg class="card__shapes" viewBox="0 0 745 448" preserveAspectRatio="none" aria-hidden="true">
    <path d="M0 192 L590 192 C665 192 720 165 745 122 L745 448 L0 448 Z" fill="var(--brand-blue)"/>
    <path d="M0 185 L590 185 C660 185 715 150 745 100 L745 122 C720 165 665 192 590 192 L0 192 Z" fill="var(--brand-red)"/>
  </svg>

  <div class="brand">
    <span class="brand__dot"></span>
    <span class="brand__name">VornaxIT</span>
  </div>

  <div class="person">
    <p class="person__name">Dariush Pelo</p>
    <p class="person__title">Managing Director</p>
  </div>

  <ul class="contact">
    <li class="contact__item">Phone number
      <svg class="contact__icon" viewBox="0 0 20 20"><path d="M9 2 C12 5 12 6 10 8 C11 11 12 12 14 13 C16 11 17 11 19 14 C16 19 12 19 8 15 C4 11 3 6 9 2 Z" fill="var(--brand-red)" transform="scale(0.9) translate(-2,1)"/></svg>
    </li>
    <li class="contact__item">Mobile number
      <svg class="contact__icon" viewBox="0 0 20 20"><rect x="5" y="1.5" width="10" height="17" rx="1.5" fill="none" stroke="var(--brand-red)" stroke-width="1.6"/><line x1="5" y1="15" x2="15" y2="15" stroke="var(--brand-red)" stroke-width="1.2"/></svg>
    </li>
    <li class="contact__item">email
      <svg class="contact__icon" viewBox="0 0 20 20"><rect x="1.5" y="4.5" width="17" height="11" fill="none" stroke="var(--brand-red)" stroke-width="1.5"/><path d="M1.5 4.5 L10 11 L18.5 4.5 M1.5 15.5 L7.5 9.5 M18.5 15.5 L12.5 9.5" fill="none" stroke="var(--brand-red)" stroke-width="1.3"/></svg>
    </li>
    <li class="contact__item">www
      <svg class="contact__icon" viewBox="0 0 20 20" fill="none" stroke="var(--brand-red)" stroke-width="1.3"><circle cx="10" cy="10" r="8.5"/><ellipse cx="10" cy="10" rx="4" ry="8.5"/><line x1="1.5" y1="10" x2="18.5" y2="10"/><line x1="3" y1="5.5" x2="17" y2="5.5"/><line x1="3" y1="14.5" x2="17" y2="14.5"/></svg>
    </li>
    <li class="contact__item contact__item--address">
      <span>Sdn. Bhd.5th Floor, Block F, Wisma LBD,No.14<br>Jalan Seri Mewah, 50470, Kuala Lumpur, Malaysia</span>
      <svg class="contact__icon" viewBox="0 0 20 32"><path d="M10 1 C4.5 1 1 5 1 9.5 C1 15 10 31 10 31 C10 31 19 15 19 9.5 C19 5 15.5 1 10 1 Z" fill="var(--brand-red)"/><circle cx="10" cy="9.5" r="3.5" fill="var(--brand-blue)"/></svg>
    </li>
  </ul>
</section>

<section class="card card--back" aria-label="Business card back">
  <svg class="card__shapes" viewBox="0 0 745 448" preserveAspectRatio="none" aria-hidden="true">
    <path d="M0 0 L745 0 L745 265 L140 265 C80 265 25 285 0 318 Z" fill="var(--brand-blue)"/>
    <path d="M0 318 C25 285 80 265 140 265 L745 265 L745 272 L140 272 C85 272 30 300 0 345 Z" fill="var(--brand-red)"/>
  </svg>

  <p class="tagline">Encrypted voice and data solutions for<br>Orbis OS, Droidex, Panelix and Bramblex devices</p>

  <div class="brand">
    <span class="brand__dot"></span>
    <span class="brand__name">VornaxIT</span>
  </div>
</section>

</body>
</html>
```